Clean Energy Brand - Business Card and Letterhead Designs

Hi, everyone! We need a graphic designer who has experience working with the energy sector. We want help designing a perfect two-sided business card and letterhead for a clean energy company we've been assisting. We have a great new logo and all of the associated files.Our client is looking for a design that is "disruptive," "future-facing," "masculine," "bold," and "empowering." The colours of the logo are navy blue and orange and are meant to stand out. We'll need all ownership and copyright paperwork as well as first proofs in a 48-hour period.

Target Market(s)

Government; Non-Profits; Clean Energy Industry; Municipalities; North American Energy Sector

Industry/Entity Type

Power Generation

Requirements
Must have
• A matching business card and letterhead design
Should not have
• Must not be from a template

```html
<!DOCTYPE html>
<html lang="en">
<head>
<meta charset="utf-8">
<title>Northvale Clean Energy – Business Card</title>
<link href="https://fonts.googleapis.com/css2?family=Poppins:wght@400;500;600&family=Roboto:wght@500;700&display=swap" rel="stylesheet">
<style>
  :root {
    --navy: #041b4a;
    --orange: #f15a29;
    --ink: #4a4a4a;
    --paper: #ffffff;
    --backdrop: #e4e4e4;
  }
  * { box-sizing: border-box; margin: 0; padding: 0; }
  html, body { width: 1125px; height: 1200px; overflow: hidden; }
  body {
    background: var(--backdrop);
    font-family: "Poppins", sans-serif;
    position: relative;
  }
  .card {
    position: absolute;
    left: 150px;
    width: 826px;
    height: 472px;
    box-shadow: 2px 3px 5px rgba(0,0,0,0.25);
    overflow: hidden;
  }
  .card--front { top: 98px; background: var(--paper); }
  .card--back { top: 630px; background: var(--navy); }

  .brand {
    position: absolute;
    left: 0;
    width: 442px;
    top: 150px;
    text-align: center;
  }
  .brand__dot {
    display: block;
    width: 46px;
    height: 46px;
    border-radius: 50%;
    background: var(--orange);
    margin: 0 auto 18px;
  }
  .brand__name {
    color: var(--navy);
    font-family: "Poppins", sans-serif;
    font-weight: 600;
    font-size: 40px;
    line-height: 1.05;
    letter-spacing: -0.5px;
  }

  .divider {
    position: absolute;
    left: 442px;
    top: 108px;
    width: 1px;
    height: 254px;
    background: var(--navy);
  }
  .contact {
    position: absolute;
    left: 472px;
    top: 102px;
    color: var(--ink);
  }
  .contact__name {
    font-family: "Roboto", sans-serif;
    font-weight: 700;
    font-size: 31px;
    color: var(--orange);
    line-height: 1.1;
  }
  .contact__title {
    font-size: 21px;
    color: var(--navy);
    line-height: 1.2;
    margin-bottom: 12px;
  }
  .contact__address {
    font-size: 18.5px;
    line-height: 1.25;
    margin-bottom: 12px;
  }
  .contact__list { list-style: none; }
  .contact__item {
    display: flex;
    align-items: center;
    font-size: 18.5px;
    height: 26px;
  }
  .contact__icon {
    width: 18px;
    height: 18px;
    margin-right: 12px;
    fill: var(--orange);
    flex: none;
  }
  .band {
    position: absolute;
    left: 0;
    bottom: 0;
    width: 826px;
    height: 12px;
  }

  .back__mark {
    position: absolute;
    left: 348px;
    top: 155px;
    width: 130px;
    height: 130px;
    border-radius: 50%;
    background: var(--orange);
  }
  .back__web {
    position: absolute;
    left: 0;
    width: 100%;
    top: 395px;
    text-align: center;
    color: #ffffff;
    font-size: 19px;
    letter-spacing: 3px;
  }
</style>
</head>
<body>

<section class="card card--front">
  <div class="brand">
    <span class="brand__dot"></span>
    <div class="brand__name">Northvale<br>Clean Energy</div>
  </div>

  <div class="divider"></div>

  <div class="contact">
    <div class="contact__name">DANIEL HARPER</div>
    <div class="contact__title">President</div>
    <div class="contact__address">2140 Birchwood Court<br>Fairbanks, Alaska 99701</div>
    <ul class="contact__list">
      <li class="contact__item">
        <svg class="contact__icon" viewBox="0 0 24 24"><path d="M6.6 10.8a15.1 15.1 0 0 0 6.6 6.6l2.2-2.2a1 1 0 0 1 1-.25 11.4 11.4 0 0 0 3.6.57 1 1 0 0 1 1 1V20a1 1 0 0 1-1 1A17 17 0 0 1 3 4a1 1 0 0 1 1-1h3.5a1 1 0 0 1 1 1c0 1.25.2 2.45.57 3.57a1 1 0 0 1-.25 1z"/></svg>
        555-214-8630
      </li>
      <li class="contact__item">
        <svg class="contact__icon" viewBox="0 0 24 24"><path d="M7 1h10a2 2 0 0 1 2 2v18a2 2 0 0 1-2 2H7a2 2 0 0 1-2-2V3a2 2 0 0 1 2-2zm0 3v14h10V4zm5 15.2a1.2 1.2 0 1 0 0 2.4 1.2 1.2 0 0 0 0-2.4z"/></svg>
        555-617-2049
      </li>
      <li class="contact__item">
        <svg class="contact__icon" viewBox="0 0 24 24"><path d="M6 2h12v5H6zM3 8h18a2 2 0 0 1 2 2v7h-4v-3H5v3H1v-7a2 2 0 0 1 2-2zm3 7h12v7H6z"/></svg>
        555-308-4172
      </li>
      <li class="contact__item">
        <svg class="contact__icon" viewBox="0 0 24 24"><path d="M2 5h20v14H2zm2 2v.4l8 5.2 8-5.2V7zm0 2.8V17h16V9.8l-8 5.2z"/></svg>
        info@northvale.com
      </li>
      <li class="contact__item">
        <svg class="contact__icon" viewBox="0 0 24 24"><path d="M12 2a10 10 0 1 0 0 20 10 10 0 0 0 0-20zm-1 17.9A8 8 0 0 1 4.2 10.2L9 15v1a2 2 0 0 0 2 2zm6.9-2.5A2 2 0 0 0 16 16h-1v-3a1 1 0 0 0-1-1H8v-2h2a1 1 0 0 0 1-1V7h2a2 2 0 0 0 2-2v-.4a8 8 0 0 1 2.9 12.8z"/></svg>
        www.northvale.com
      </li>
    </ul>
  </div>

  <svg class="band" viewBox="0 0 826 12" preserveAspectRatio="none">
    <polygon points="0,0 540,0 536,12 0,12" fill="var(--orange)"/>
    <polygon points="546,0 826,0 826,12 542,12" fill="var(--navy)"/>
  </svg>
</section>

<section class="card card--back">
  <span class="back__mark"></span>
  <div class="back__web">WWW.NORTHVALECLEANENERGY.COM</div>
</section>

</body>
</html>
```